Designer and consultant for professionals/businesses and manufacturers in the kitchen and bath in...

I have 30 years of design experience, and 19 of those years within the marketing team of a national cabinet manufacturer. This role gave me the opportunity to consult and design for kitchen/bath businesses, from boutique to multi-store national scale. My services include layout and spatial planning, individual display design, and product design for cabinet manufacturers. From showrooms, to trade shows to integrated design collections. I would like to see designs that convey professionalism, as well as an appeal to the creative designer mind!

Target Market(s)

Kitchen and bath dealers, as well as mid-scale multi-store home centers. Cabinet manufacturers, Trade Show agencies.

Industry/Entity Type

Kitchen

Contact Information for Business Card

Serving Kitchen and Bath Businesses

Logo Text

MT (initials for business name)

Font styles to use
Serif
Sans Serif
Decorative

Colors
e34197

Requirements
Must have
• Marlowe Tavish Design and Consulting, Inc. (business name)
• marlowe@mtvantra.com (email)
• 917-555-0148 (phone)
• mtvantra.com (website)
Nice to have
• Inclusions of geometric shapes; particularly a 30/15 degree triangle and circle(s)
• 2 colors
Should not have
• Not too artsy!

```html
<!DOCTYPE html>
<html lang="en">
<head>
<meta charset="utf-8">
<title>Marlowe Tavish Design and Consulting, Inc. — Business Card</title>
<link rel="stylesheet" href="https://fonts.googleapis.com/css2?family=Rokkitt:wght@600&family=Lato:wght@400;700&display=swap">
<style>
  :root {
    --stage: #2e2e2e;
    --card-white: #ffffff;
    --brand-red: #b85f5f;
    --brand-brown: #5a3838;
    --ink-grey: #6b6b6b;
    --ink-dark: #3a3a3a;
    --on-red: #ffffff;
  }
  * { box-sizing: border-box; margin: 0; padding: 0; }
  html, body {
    width: 1200px; height: 866px; overflow: hidden;
    background: var(--stage);
  }
  .canvas {
    width: 1200px; height: 866px;
    display: flex; flex-direction: column;
    align-items: center; justify-content: space-evenly;
  }
  .card {
    position: relative;
    width: 640px; height: 366px;
    overflow: hidden;
    box-shadow: 0 6px 18px rgba(0,0,0,.45);
  }

  /* Front */
  .card-front { background: var(--card-white); }
  .card-front .edge-band {
    position: absolute; left: 0; right: 0; bottom: 0; height: 12px;
    background: var(--brand-red);
  }
  .contact-list {
    position: absolute; left: 40px; top: 232px;
    list-style: none;
    font-family: "Lato", sans-serif; font-size: 16px;
    color: var(--ink-dark); line-height: 26px;
  }
  .contact-list li { display: flex; align-items: center; gap: 10px; white-space: nowrap; }
  .contact-list svg { width: 14px; height: 14px; fill: var(--ink-dark); flex: none; }
  .brand-disc {
    position: absolute; right: 70px; top: 36px;
    width: 132px; height: 132px; border-radius: 50%;
    background: var(--brand-brown);
    border: 4px solid var(--brand-red);
  }
  .identity-text {
    position: absolute; right: 40px; top: 178px;
    text-align: right;
  }
  .brand-name {
    font-family: "Rokkitt", serif; font-weight: 600;
    font-size: 40px; line-height: 1; color: var(--brand-brown);
    letter-spacing: .5px; white-space: nowrap;
  }
  .brand-tagline {
    margin-top: 8px;
    font-family: "Lato", sans-serif; font-size: 11px;
    letter-spacing: 3.2px; text-transform: uppercase;
    color: var(--ink-grey); white-space: nowrap;
  }

  /* Back */
  .card-back { background: var(--brand-red); }
  .back-mark {
    position: absolute; left: 50%; top: 78px; transform: translateX(-50%);
    display: flex; align-items: center; gap: 16px;
  }
  .back-disc {
    width: 58px; height: 58px; border-radius: 50%;
    border: 3px solid var(--on-red); flex: none;
  }
  .back-name {
    font-family: "Rokkitt", serif; font-weight: 600;
    font-size: 38px; color: var(--on-red); white-space: nowrap;
  }
  .service-line {
    position: absolute; left: 0; right: 0; top: 232px;
    text-align: center;
    font-family: "Lato", sans-serif; font-size: 18px;
    letter-spacing: .6px; text-transform: uppercase;
    color: var(--on-red);
  }
</style>
</head>
<body>
<main class="canvas">

  <section class="card card-front" aria-label="Business card front">
    <div class="brand-disc" aria-hidden="true"></div>

    <div class="identity-text">
      <p class="brand-name">Marlowe Tavish</p>
      <p class="brand-tagline">Design and Consulting, Inc.</p>
    </div>

    <ul class="contact-list">
      <li>
        <svg viewBox="0 0 16 16" aria-hidden="true"><path d="M3.5 1.5l2.5 0 1.2 3.2-1.6 1.2a8 8 0 0 0 4.5 4.5l1.2-1.6 3.2 1.2v2.5a1.5 1.5 0 0 1-1.6 1.5A12.5 12.5 0 0 1 2 3.1 1.5 1.5 0 0 1 3.5 1.5z"/></svg>
        <span>917-555-0148</span>
      </li>
      <li>
        <svg viewBox="0 0 16 16" aria-hidden="true"><path d="M1 3h14v10H1z M2 4v.4l6 4.2 6-4.2V4z" fill-rule="evenodd"/></svg>
        <span>marlowe@mtvantra.com</span>
      </li>
      <li>
        <svg viewBox="0 0 16 16" aria-hidden="true"><circle cx="8" cy="8" r="7"/><path d="M1.5 8h13M8 1c2.5 2.5 2.5 11.5 0 14M8 1c-2.5 2.5-2.5 11.5 0 14" stroke="#fff" stroke-width="1" fill="none"/></svg>
        <span>www.mtvantra.com</span>
      </li>
    </ul>

    <div class="edge-band" aria-hidden="true"></div>
  </section>

  <section class="card card-back" aria-label="Business card back">
    <div class="back-mark">
      <div class="back-disc" aria-hidden="true"></div>
      <p class="back-name">Marlowe Tavish</p>
    </div>
    <p class="service-line">Serving Kitchen &amp; Bath Business</p>
  </section>

</main>
</body>
</html>
```